R&t Subterra

We specialize in CIPP pipe lining but do other underground utilities trenchless as well.

Target Market(s)

Trenchless sewer replacement

Contact Information for Business Card

Gavin Holtby 715-482-6130 Pine Hollow, WI

```html
<!DOCTYPE html>
<html lang="en">
<head>
<meta charset="utf-8">
<title>R&amp;T Subterra – Business Card</title>
<link href="https://fonts.googleapis.com/css2?family=Lato:wght@400;700;900&family=Montserrat:wght@500;800&display=swap" rel="stylesheet">
<style>
  :root {
    --stage: #1f1f1f;
    --brand-blue: #2f87c6;
    --brand-blue-light: #56b2e4;
    --sky: #8fc7e8;
    --white: #ffffff;
    --grey: #9a9a9a;
  }
  html, body {
    margin: 0;
    padding: 0;
    width: 1200px;
    height: 825px;
    overflow: hidden;
    background: var(--stage);
  }
  .sheet {
    width: 1200px;
    height: 825px;
    display: flex;
    align-items: center;
    justify-content: center;
    gap: 44px;
  }
  .card {
    position: relative;
    width: 540px;
    height: 308px;
    border-radius: 22px;
    overflow: hidden;
  }
  .card-front {
    background: radial-gradient(ellipse 60% 65% at 50% 50%, #ffffff 0%, #e3f1fa 45%, var(--sky) 100%);
  }
  .card-back {
    background: var(--white);
  }
  .brand {
    position: absolute;
    display: flex;
    align-items: center;
    gap: 12px;
  }
  .brand-dot {
    width: 46px;
    height: 46px;
    border-radius: 50%;
    background: var(--brand-blue);
    flex: none;
  }
  .brand-name {
    font-family: "Montserrat", sans-serif;
    font-weight: 800;
    color: var(--brand-blue);
    letter-spacing: 1px;
    white-space: nowrap;
  }
  .card-front .brand {
    left: 50%;
    top: 50%;
    transform: translate(-50%, -50%);
  }
  .card-front .brand-name { font-size: 36px; }
  .card-back .brand {
    left: 62px;
    top: 74px;
  }
  .card-back .brand-dot { width: 34px; height: 34px; }
  .card-back .brand-name { font-size: 24px; }
  .wave {
    position: absolute;
    inset: 0;
    width: 100%;
    height: 100%;
  }
  .contact {
    position: absolute;
    right: 36px;
    top: 148px;
    text-align: right;
    color: var(--white);
    font-family: "Lato", sans-serif;
  }
  .contact-name {
    margin: 0 0 6px;
    font-weight: 900;
    font-size: 25px;
    letter-spacing: 0.5px;
    text-transform: uppercase;
  }
  .contact-line {
    margin: 0 0 4px;
    display: flex;
    align-items: center;
    justify-content: flex-end;
    gap: 8px;
  }
  .contact-phone { font-size: 17px; font-weight: 400; }
  .contact-place { font-size: 14px; font-weight: 400; }
  .icon { width: 12px; height: 14px; flex: none; }
</style>
</head>
<body>
  <main class="sheet">
    <section class="card card-front" aria-label="Card front">
      <div class="brand">
        <span class="brand-dot"></span>
        <span class="brand-name">R&amp;T SUBTERRA</span>
      </div>
    </section>

    <section class="card card-back" aria-label="Card back">
      <svg class="wave" viewBox="0 0 540 308" aria-hidden="true">
        <path d="M0,252 C150,246 240,215 305,150 C370,85 440,62 540,55 L540,308 L0,308 Z" fill="var(--brand-blue)"/>
        <path d="M0,252 C150,246 240,215 305,150 C370,85 440,62 540,55" fill="none" stroke="var(--brand-blue-light)" stroke-width="5"/>
        <path d="M92,240 C175,232 238,200 265,160 C246,206 182,236 92,240 Z" fill="var(--grey)"/>
      </svg>

      <div class="brand">
        <span class="brand-dot"></span>
        <span class="brand-name">R&amp;T SUBTERRA</span>
      </div>

      <div class="contact">
        <p class="contact-name">Gavin Holtby</p>
        <p class="contact-line contact-phone">
          <span>715-482-6130</span>
          <svg class="icon" viewBox="0 0 12 14" aria-hidden="true">
            <rect x="2" y="0.8" width="8" height="12.4" rx="1.5" fill="none" stroke="#fff" stroke-width="1.4"/>
            <circle cx="6" cy="11" r="0.9" fill="#fff"/>
          </svg>
        </p>
        <p class="contact-line contact-place">
          <span>Pine Hollow, WI</span>
          <svg class="icon" viewBox="0 0 12 14" aria-hidden="true">
            <path d="M6,13.5 C3,9.5 1.5,7.2 1.5,5 A4.5,4.5 0 0 1 10.5,5 C10.5,7.2 9,9.5 6,13.5 Z" fill="#fff"/>
            <circle cx="6" cy="5" r="1.7" fill="var(--brand-blue)"/>
          </svg>
        </p>
      </div>
    </section>
  </main>
</body>
</html>
```